LORM Business Card Design Project

Company Name: LORM (Bright Harbor Computing Solutions) PGH.
Office Address: Office No 718, Saffron Crest Tower, Palmwood Garden Heights, Dubai, U.A.E
Company line of business:
1) Currently we have a POS solution for retail outlets like duty free shops, supermarkets, department stores etc... The solution is deployed in Coastline Travel Retail on 350 POS and in Sandgate Airport Retail on 100 POS. So our main line of business is the deployment of this solution in retail outlets locally or regionally. We have already deployed the solution in India and Australia.
2) Integration of other third party POS systems with an online credit authorization netwotk in the UAE. This will enable POS applications to connect directly to the acquiring banks without needing an EFT terminal like Paxtrel or Movarski. The credit card payment is completed at the POS.
3) Other solutions that are targeting retail outlets like mobile POS, queue busting solutions, stock taking solutions using hand held devices, transaction capture systems, etc...
4) Other IT services like support of call center solutions from Northwind Callworks and development of new solutions as per customer requirements.
We need a business card design for the company. We don't have any specific requirements and will eave up to the designers to come up with creative designs. At the moment we still don't have a letter head design and the only thing that we have is the company logo that we will upload shortly.
Updates
Dear All,
I just uploaded the logo source files. I am sorry for the delay.
Regards
Samir Odwani
I would like the business cards to have the following details:
Company Tel No
Company Fax No
Company Website Address
Employee Name
Employee Title
Employee Mobile Number
Employee Email Address

```html
<!DOCTYPE html>
<html lang="en">
<head>
<meta charset="utf-8">
<title>LORM Business Card</title>
<link rel="stylesheet" href="https://fonts.googleapis.com/css2?family=Source+Sans+3:wght@400;600;700&display=swap">
<style>
  :root {
    --backdrop: #d8d3cd;
    --card: #ffffff;
    --ink: #2e2e2e;
    --ink-soft: #555555;
    --blue-light: #20a8e6;
    --blue-deep: #0a5aa6;
    --swoosh-dark: #1c1c1c;
    --brand-dot: #1577c4;
    --contact-text: #ffffff;
  }
  * { box-sizing: border-box; margin: 0; padding: 0; }
  html, body {
    width: 1200px; height: 390px; overflow: hidden;
    background: var(--backdrop);
    font-family: "Source Sans 3", "Segoe UI", sans-serif;
  }
  .canvas { position: relative; width: 1200px; height: 390px; }
  .card {
    position: absolute; top: 50px; width: 508px; height: 290px;
    background: var(--card);
    box-shadow: 3px 4px 8px rgba(0,0,0,0.35);
    overflow: hidden;
  }
  .card-front { left: 50px; }
  .card-back { left: 642px; }

  .brand {
    position: absolute; display: flex; align-items: center; gap: 10px;
    color: var(--ink); font-weight: 600; letter-spacing: 2px;
  }
  .brand-dot { border-radius: 50%; background: var(--brand-dot); flex: none; }
  .card-front .brand { left: 34px; top: 52px; font-size: 44px; line-height: 1; }
  .card-front .brand-dot { width: 26px; height: 26px; }
  .card-back .brand { left: 50%; top: 50%; transform: translate(-50%, -50%); font-size: 58px; line-height: 1; }
  .card-back .brand-dot { width: 34px; height: 34px; }

  .address {
    position: absolute; right: 26px; top: 44px;
    text-align: right; font-size: 13.5px; line-height: 19px; color: var(--ink-soft);
  }
  .swoosh { position: absolute; left: 0; top: 0; width: 508px; height: 290px; }

  .person {
    position: absolute; left: 50px; top: 220px;
    font-size: 13px; color: var(--ink-soft);
  }
  .person-name { font-size: 16.5px; font-weight: 700; color: var(--ink-soft); }

  .contacts {
    position: absolute; right: 26px; top: 196px;
    list-style: none; text-align: right;
    font-size: 12.5px; line-height: 15.5px; color: var(--contact-text);
  }
  .contacts li { display: flex; justify-content: flex-end; align-items: center; gap: 4px; }
  .contacts svg { width: 10px; height: 10px; fill: var(--contact-text); flex: none; }
</style>
</head>
<body>
<main class="canvas">
  <section class="card card-front">
    <svg class="swoosh" viewBox="0 0 508 290" aria-hidden="true">
      <defs>
        <linearGradient id="band-blue" x1="0" y1="0" x2="1" y2="0">
          <stop offset="0" stop-color="var(--blue-light)"/>
          <stop offset="0.55" stop-color="#1583cf"/>
          <stop offset="1" stop-color="var(--blue-deep)"/>
        </linearGradient>
      </defs>
      <path d="M0,248 C110,292 300,232 508,140 L508,290 L0,290 Z" fill="url(#band-blue)"/>
      <path d="M0,228 C50,262 170,250 322,208 C180,256 60,272 0,240 Z" fill="var(--swoosh-dark)"/>
    </svg>

    <div class="brand"><span class="brand-dot"></span>LORM</div>

    <address class="address">
      Office No 718,<br>
      Saffron Crest Tower,<br>
      Palmwood Garden Heights,<br>
      Dubai, U.A.E
    </address>

    <p class="person"><span class="person-name">Name</span> / Title</p>

    <ul class="contacts">
      <li>123-456-7890
        <svg viewBox="0 0 10 10"><path d="M2 0.5 L3.8 2.6 L2.9 3.7 C3.5 5 4.8 6.4 6.2 7 L7.3 6.1 L9.5 7.9 L8.4 9.5 C4.5 9.3 0.6 5.4 0.5 1.6 Z"/></svg></li>
      <li>123-456-7890
        <svg viewBox="0 0 10 10"><path d="M2.5 0 H7.5 V10 H2.5 Z M3.3 1 V7.3 H6.7 V1 Z M4.5 8 H5.5 V9 H4.5 Z" fill-rule="evenodd"/></svg></li>
      <li>123-456-7890
        <svg viewBox="0 0 10 10"><path d="M2.5 0.5 H7.5 V3.5 H2.5 Z M0.5 4 H9.5 V8 H7.5 V9.5 H2.5 V8 H0.5 Z"/></svg></li>
      <li>www.lormsite.com
        <svg viewBox="0 0 10 10"><path d="M5 0.5 A4.5 4.5 0 1 0 5 9.5 A4.5 4.5 0 1 0 5 0.5 Z M5 1.5 A3.5 3.5 0 1 1 5 8.5 A3.5 3.5 0 1 1 5 1.5 Z M4.6 1 H5.4 V9 H4.6 Z M1 4.6 H9 V5.4 H1 Z" fill-rule="evenodd"/></svg></li>
      <li>lorm@email.com
        <svg viewBox="0 0 10 10"><text x="5" y="8.6" text-anchor="middle" font-size="10" font-weight="700" font-family="Arial, sans-serif">@</text></svg></li>
    </ul>
  </section>

  <section class="card card-back">
    <div class="brand"><span class="brand-dot"></span>LORM</div>
  </section>
</main>
</body>
</html>
```